Business card design for engineering firm specializing in defense industry.

We need a professional business card design. Something simple but stands out. We are an engineering company specializing in composites in the defense industry.
Industry/Entity Type
Defense
Contact Information for Business Card
A simple black business card with the Varlonix yellow color is what we had in mind but open for other designs.
Colors
ffc214

```html
<!DOCTYPE html>
<html lang="en">
<head>
<meta charset="utf-8">
<title>Varlonix Business Card</title>
<link href="https://fonts.googleapis.com/css2?family=Saira:wght@600&display=swap" rel="stylesheet">
<style>
  :root {
    --backdrop: #c9c9c9;
    --card-black: #0b0b0b;
    --weave-dark: #111111;
    --weave-light: #2a2a2a;
    --brand-yellow: #ffc214;
    --band-yellow: #f0b411;
    --logo-white: #ffffff;
    --url-ink: #141414;
  }
  * { margin: 0; padding: 0; box-sizing: border-box; }
  html, body {
    width: 1200px;
    height: 900px;
    overflow: hidden;
    background: var(--backdrop);
  }
  .canvas {
    position: relative;
    width: 1200px;
    height: 900px;
  }
  .business-card {
    position: absolute;
    left: 180px;
    top: 210px;
    width: 840px;
    height: 480px;
    background: var(--card-black);
    overflow: hidden;
    box-shadow: 0 10px 30px rgba(0, 0, 0, 0.25);
  }
  .carbon-texture {
    position: absolute;
    inset: 0;
    width: 100%;
    height: 100%;
  }
  .brand-lockup {
    position: absolute;
    left: 0;
    right: 0;
    top: 110px;
    display: flex;
    align-items: center;
    justify-content: center;
    gap: 22px;
  }
  .brand-square {
    width: 46px;
    height: 46px;
    background: var(--brand-yellow);
  }
  .brand-name {
    font-family: "Saira", sans-serif;
    font-weight: 600;
    font-size: 78px;
    line-height: 1;
    letter-spacing: 1px;
    color: var(--logo-white);
  }
  .contact-band {
    position: absolute;
    left: 0;
    right: 0;
    top: 318px;
    height: 64px;
    background: var(--band-yellow);
    display: flex;
    align-items: center;
    justify-content: center;
  }
  .website {
    font-family: "Saira", sans-serif;
    font-weight: 600;
    font-size: 30px;
    letter-spacing: 1px;
    color: var(--url-ink);
  }
</style>
</head>
<body>
  <main class="canvas">
    <section class="business-card">
      <svg class="carbon-texture" viewBox="0 0 840 480" preserveAspectRatio="none" role="img" aria-label="Black woven carbon fibre surface with a softly lit diagonal panel">
        <defs>
          <linearGradient id="weaveShade" x1="0" y1="0" x2="1" y2="1">
            <stop offset="0" stop-color="var(--weave-light)"/>
            <stop offset="0.55" stop-color="var(--weave-dark)"/>
            <stop offset="1" stop-color="var(--card-black)"/>
          </linearGradient>
        </defs>
        <rect width="840" height="480" fill="url(#weaveShade)"/>
        <polygon points="0,60 520,0 840,180 840,320 0,320" fill="#1b1b1b" opacity="0.55"/>
      </svg>

      <div class="brand-lockup">
        <span class="brand-square" aria-hidden="true"></span>
        <span class="brand-name">Varlonix</span>
      </div>

      <div class="contact-band">
        <span class="website">WWW.VARLONIX.COM</span>
      </div>
    </section>
  </main>
</body>
</html>
```